RWT Installations Ltd Business Cards

We need a business card with our business logo. We provide window and door installations on high-rises in west coast British Colombia, Canada.

I would like my business information and details on one side of the card, and the other side the company name with logo

Target Market(s)

General Contractors

Industry/Entity Type

Construction

Contact Information for Business Card

one side i want my company name and logo in the dark theme logo that i provided

Requirements
Must have
• Tomas Verelund, 15559284016, RWTInstallations@mailvera.example, 1408-5192 Pellow Avenue Burnaby BC, V0X 1Z9, Owner & Manager

```html
<!DOCTYPE html>
<html lang="en">
<head>
<meta charset="utf-8">
<title>RWT Installations Ltd – Business Cards</title>
<link rel="stylesheet" href="https://fonts.googleapis.com/css2?family=Open+Sans:wght@400;600;700&display=swap">
<style>
  :root {
    --backdrop: #dcdad6;
    --card: #161616;
    --brand-blue: #29a8e0;
    --steel-grey: #9b9b9b;
    --text-light: #f2f2f2;
    --text-muted: #cfcfcf;
  }
  * { box-sizing: border-box; margin: 0; padding: 0; }
  html, body {
    width: 1200px;
    height: 780px;
    overflow: hidden;
  }
  body {
    background: var(--backdrop);
    font-family: "Open Sans", Arial, sans-serif;
    position: relative;
  }
  .card {
    position: absolute;
    top: 235px;
    width: 540px;
    height: 310px;
    background: var(--card);
    border-radius: 3px;
    box-shadow: 0 10px 26px rgba(0, 0, 0, 0.28);
    overflow: hidden;
  }
  .card--contact { left: 40px; }
  .card--brand { left: 620px; }

  /* brand lockup */
  .brand {
    display: flex;
    align-items: center;
    gap: 12px;
    color: var(--brand-blue);
    font-weight: 700;
    text-transform: uppercase;
    white-space: nowrap;
  }
  .brand__mark {
    background: var(--brand-blue);
    flex: none;
  }
  .card--contact .brand {
    position: absolute;
    top: 44px;
    left: 150px;
    font-size: 20px;
    letter-spacing: 0.5px;
  }
  .card--contact .brand__mark { width: 26px; height: 26px; }

  .card--brand .brand {
    position: absolute;
    top: 50%;
    left: 50%;
    transform: translate(-50%, -50%);
    font-size: 29px;
    letter-spacing: 1px;
  }
  .card--brand .brand__mark { width: 40px; height: 40px; }

  /* person */
  .person {
    position: absolute;
    top: 132px;
    left: 34px;
    width: 190px;
    text-align: right;
  }
  .person__name {
    color: var(--brand-blue);
    font-size: 19px;
    font-weight: 700;
    text-transform: uppercase;
    white-space: nowrap;
  }
  .person__role {
    color: var(--text-muted);
    font-size: 12.5px;
    margin-top: 2px;
  }

  .divider {
    position: absolute;
    top: 118px;
    left: 240px;
    width: 1px;
    height: 96px;
    background: linear-gradient(to bottom, transparent, var(--brand-blue) 30%, var(--brand-blue) 70%, transparent);
  }

  /* contacts */
  .contacts {
    position: absolute;
    top: 126px;
    left: 256px;
    list-style: none;
  }
  .contacts__item {
    display: flex;
    align-items: center;
    gap: 7px;
    color: var(--text-light);
    font-size: 12.5px;
    line-height: 1;
    margin-bottom: 11px;
    white-space: nowrap;
  }
  .contacts__icon { width: 12px; height: 12px; flex: none; }

  /* address band */
  .address-band {
    position: absolute;
    left: 0;
    right: 0;
    bottom: 0;
    height: 34px;
    background: var(--steel-grey);
    display: flex;
    align-items: center;
    padding-left: 34px;
    color: var(--text-light);
    font-size: 12.5px;
    letter-spacing: 0.2px;
  }
</style>
</head>
<body>

  <section class="card card--contact" aria-label="Contact side">
    <div class="brand">
      <span class="brand__mark"></span>
      <span class="brand__name">RWT Installations Ltd</span>
    </div>

    <div class="person">
      <p class="person__name">Tomas Verelund</p>
      <p class="person__role">Owner &amp; Manager</p>
    </div>

    <div class="divider"></div>

    <ul class="contacts">
      <li class="contacts__item">
        <svg class="contacts__icon" viewBox="0 0 24 24" aria-hidden="true">
          <path fill="#29a8e0" d="M6.6 10.8a15.1 15.1 0 0 0 6.6 6.6l2.2-2.2a1 1 0 0 1 1-.25 11.4 11.4 0 0 0 3.6.57 1 1 0 0 1 1 1V20a1 1 0 0 1-1 1A17 17 0 0 1 3 4a1 1 0 0 1 1-1h3.5a1 1 0 0 1 1 1c0 1.25.2 2.45.57 3.57a1 1 0 0 1-.25 1z"/>
        </svg>
        <span>15559284016</span>
      </li>
      <li class="contacts__item">
        <svg class="contacts__icon" viewBox="0 0 24 24" aria-hidden="true">
          <rect x="2" y="5" width="20" height="14" rx="1.5" fill="#29a8e0"/>
          <path d="M3 6.5l9 6.5 9-6.5" fill="none" stroke="#161616" stroke-width="1.8"/>
        </svg>
        <span>RWTInstallations@mailvera.example</span>
      </li>
      <li class="contacts__item">
        <svg class="contacts__icon" viewBox="0 0 24 24" aria-hidden="true">
          <circle cx="12" cy="12" r="10" fill="#29a8e0"/>
          <path d="M2 12h20M12 2c3 3 3 17 0 20M12 2c-3 3-3 17 0 20" fill="none" stroke="#161616" stroke-width="1.5"/>
        </svg>
        <span>www.rwtinstallations.example</span>
      </li>
    </ul>

    <div class="address-band">
      <span>1408-5192 Pellow Avenue Burnaby BC, V0X 1Z9</span>
    </div>
  </section>

  <section class="card card--brand" aria-label="Brand side">
    <div class="brand">
      <span class="brand__mark"></span>
      <span class="brand__name">RWT Installations Ltd</span>
    </div>
  </section>

</body>
</html>
```